Corporate Business Card

Very professional, Modern, Not to busy, include phone address email, website
(253) 555-0174, 61807 19th Street N, Kent, WA 98517, marcus@kestrelbayholding.com, brelvanindustries.com

Target Market(s)

Manufacturing

Industry/Entity Type

Aero, machining, manufacturing, Off road racing

Contact Information for Business Card

Phone, address email, website

```html
<!DOCTYPE html>
<html lang="en">
<head>
<meta charset="utf-8">
<title>Brelvan Industries – Business Card</title>
<link href="https://fonts.googleapis.com/css2?family=Roboto:wght@400;700&display=swap" rel="stylesheet">
<style>
  :root {
    --bg: #e3e3e3;
    --paper: #f6f6f6;
    --navy: #1c3a70;
    --ink: #2a2a2a;
    --white: #ffffff;
  }
  * { box-sizing: border-box; margin: 0; padding: 0; }
  html, body {
    width: 1200px; height: 930px; overflow: hidden;
    background: var(--bg);
    font-family: "Roboto", Arial, sans-serif;
  }
  .stage {
    width: 1200px; height: 930px;
    display: flex; align-items: center; justify-content: center; gap: 48px;
  }
  .card {
    width: 500px; height: 286px;
    position: relative;
    box-shadow: 0 6px 18px rgba(0,0,0,0.12);
  }
  .card--front { background: var(--paper); }
  .card--back {
    background: var(--navy);
    display: flex; align-items: center; justify-content: center;
  }
  .wordmark {
    font-weight: 700;
    letter-spacing: 1px;
    text-transform: uppercase;
    line-height: 1;
    text-align: center;
  }
  .card--front .wordmark {
    position: absolute; top: 58px; left: 0; right: 0;
    color: var(--navy); font-size: 34px;
  }
  .card--back .wordmark { color: var(--white); font-size: 38px; }
  .contact {
    position: absolute; top: 150px; left: 0; right: 0;
    display: flex; justify-content: center; align-items: stretch; gap: 16px;
    color: var(--ink); font-size: 12.5px; line-height: 1.45;
  }
  .contact__address { text-align: right; }
  .contact__divider { width: 1px; background: var(--ink); }
  .contact__list { list-style: none; }
  .contact__list li { display: flex; align-items: center; gap: 6px; }
  .contact__icon { width: 11px; height: 11px; fill: var(--navy); flex: none; }
</style>
</head>
<body>
<main class="stage">
  <section class="card card--front" aria-label="Business card front">
    <p class="wordmark">Brelvan Industries</p>
    <div class="contact">
      <address class="contact__address" style="font-style:normal">
        61807 19th Street N<br>Kent, WA 98517
      </address>
      <span class="contact__divider"></span>
      <ul class="contact__list">
        <li>
          <svg class="contact__icon" viewBox="0 0 24 24" aria-hidden="true"><path d="M6.6 10.8a15.1 15.1 0 0 0 6.6 6.6l2.2-2.2a1 1 0 0 1 1-.25 11.4 11.4 0 0 0 3.6.57 1 1 0 0 1 1 1V20a1 1 0 0 1-1 1A17 17 0 0 1 3 4a1 1 0 0 1 1-1h3.5a1 1 0 0 1 1 1c0 1.25.2 2.45.57 3.57a1 1 0 0 1-.25 1z"/></svg>
          (253) 555-0174
        </li>
        <li>
          <svg class="contact__icon" viewBox="0 0 24 24" aria-hidden="true"><path d="M2 5h20v14H2z M2 5l10 8 10-8" fill="none" stroke="#1c3a70" stroke-width="2.2"/></svg>
          marcus@kestrelbayholding.com
        </li>
        <li>
          <svg class="contact__icon" viewBox="0 0 24 24" aria-hidden="true"><circle cx="12" cy="12" r="10" fill="none" stroke="#1c3a70" stroke-width="2"/><path d="M2 12h20M12 2c3 3 3 17 0 20M12 2c-3 3-3 17 0 20" fill="none" stroke="#1c3a70" stroke-width="1.6"/></svg>
          www.brelvanindustries.com
        </li>
      </ul>
    </div>
  </section>
  <section class="card card--back" aria-label="Business card back">
    <p class="wordmark">Brelvan Industries</p>
  </section>
</main>
</body>
</html>
```